Custom Header Designs - Automotive Parts - Alternator & Starter

We need 8 Header/Hero designs that will be used on our website. We are a company based in Montreal Canada and we re-manufacture Alternators and Starters for all types of vehicles. We offer a premium product and we are looking for premium designs that reflect the look of our packaging and the look of our website. Essentially we specialize in the sale and manufacture of two specific parts that go on all types of vehicles, Alternators and Starters. All text on these designs need to be editable as we will need to translate them to French once we get the source files.
Here are some websites of our competitors so you can draw some inspiration and see what our industry/business is all about:
https://www.qelvorparts.com/
https://www.zentrihaul.com/
Article that describes a remanufactured product, https://www.wombrixo.com/articles/starters-and-alternators-reman-vs-new.html
Our packaging is modern, sleek and professional. Our website is a B2B E-Commerce Site as well as an info site to promote our products. It is clean and minimal but we want the header/hero designs to help it stand out. Our main colors are blue and gray (as seen in our logo), but you can use whatever you like to compliment these colors.
Our packaging design was done on PixelTroupe, here is the link to that project so that you can see the packaging look and use any of the info that is from that project.
https://jobs.pixeltroupe.ca/job/5829463
The 8 Header/Hero designs will be used in the following areas, I have included a brief description of what we are looking for:
1 - Homepage Header/Hero image - This will be the homepage hero image therefore it should summarize the info described below. We offer premium quality re-manufactured alternators and starters. We are a wholesaler/distributor that services major auto-part stores with these quality products.
2 - General Product Header/Hero image - This image will be used as a header where the customer can learn general info about our products and any custom work we can do. This page will have a section where you can click to learn more about our individual product lines (links to product specific pages mentioned below) and a description of the custom work we can perform. We offer a two year manufacturers warranty.
3 - Alternator Product Header/Hero image - This image will be used to showcase our Alternator Product Line. Its purpose is to promote and advertise our premium re-manufactured alternators. This page will provide detailed info about our alternator re-manufacturing process and describe why our alternators are great.
4 - Starter Product Header/Hero image - This image will be used to showcase our Starter Product Line. Its purpose is to promote and advertise our premium re-manufactured starters. This page will provide detailed info about our starter re-manufacturing process and describe why our starters are great.
5 - General Header/Hero Image - This image will be used in most of our standard pages like our terms and conditions, privacy policy, warranty policy, our company page, etc. It needs to relate to the industry but be general enough so that we could use it in multiple areas
6 - Online Ordering Header image - This image will be used in our B2B area to introduce our customers to the Online Ordering system, its purpose is to advertise and explain some of the features of the Online Ordering system.
7 - B/O Re-Manufacture & Return Header Image - This image will be used in our B2B area to explain and advertise to our customers how our Backorder/R&R process works on our website. Essentially if we do not have the remanufactured part in stock but we have the core you could put the product on Backorder and we will remanufacture it in a few hours. If for any reason (rare vehicle, old vehicle, etc.) we do not have the core we will R&R (Remanufacture and Return) the customers core for them.
8 - Bulk Ordering Form Header Image - This image will be used in our B2B area to explain and advertise to our customers how our Bulk Ordering Form works on our website.
These hero/header images will be going on a Plankly/TillNest website and I am suggesting these images have a size of 1600 x 500, but we will take any other suggestions from the designers as you are the experts.
I have included a zip file that includes images of various elements that will help you in the design process.
Target Market(s)
Educate consumers about our products and attract auto supply chains to become distributors of our products.
Industry/Entity Type
Automotive Part

```html
<!DOCTYPE html>
<html lang="en">
<head>
<meta charset="utf-8">
<title>Ampvero – Alternators &amp; Starters</title>
<link rel="stylesheet" href="https://fonts.googleapis.com/css2?family=Montserrat:wght@800&family=Roboto:wght@300;400;500;700&display=swap">
<style>
  :root {
    --blue-deep: #0d2a8f;
    --blue-royal: #1538a8;
    --ink-blue: #1b3fa0;
    --white: #ffffff;
    --rule: rgba(255,255,255,0.35);
  }
  * { margin: 0; padding: 0; box-sizing: border-box; }
  html, body { width: 1200px; height: 375px; overflow: hidden; background: var(--white); }
  .hero {
    position: relative;
    width: 1200px;
    height: 375px;
    overflow: hidden;
    font-family: "Roboto", Arial, sans-serif;
    color: var(--white);
  }
  .hero__shapes { position: absolute; inset: 0; width: 1200px; height: 375px; }

  .brand {
    position: absolute; left: 14px; top: 44px;
    display: flex; align-items: center; gap: 8px;
  }
  .brand__dot { width: 48px; height: 48px; border-radius: 50%; background: var(--ink-blue); }
  .brand__name {
    font-family: "Montserrat", Arial, sans-serif; font-weight: 800;
    font-size: 27px; color: var(--ink-blue); letter-spacing: -0.5px;
  }

  .headline {
    position: absolute; left: 64px; top: 236px;
    font-family: "Montserrat", Arial, sans-serif; font-weight: 800;
    font-size: 44px; line-height: 51px; letter-spacing: 0;
  }

  .badge__ring {
    position: absolute; left: 864px; top: 2px; width: 128px; height: 128px;
    border-radius: 50%; border: 1px solid var(--rule);
  }
  .badge {
    position: absolute; left: 879px; top: 17px; width: 98px; height: 98px;
    border-radius: 50%; background: var(--blue-royal);
    display: flex; flex-direction: column; align-items: center; justify-content: center;
    text-align: center;
  }
  .badge__value { font-size: 27px; font-weight: 400; line-height: 30px; }
  .badge__label { font-size: 13.5px; font-weight: 500; line-height: 17px; }

  .social { position: absolute; top: 27px; left: 1060px; display: flex; gap: 8px; }
  .social__dot { width: 22px; height: 22px; border-radius: 50%; background: var(--white); }

  .intro {
    position: absolute; left: 781px; top: 169px; width: 320px;
    text-align: center; font-size: 16.5px; font-weight: 300; line-height: 21.7px;
  }

  .contact {
    position: absolute; left: 762px; top: 349px; font-size: 16px; font-weight: 400;
  }
  .contact strong { font-weight: 700; }
  .site {
    position: absolute; left: 1018px; top: 349px; font-size: 16px; font-weight: 400;
    color: var(--ink-blue);
  }
</style>
</head>
<body>
<div class="hero">
  <svg class="hero__shapes" viewBox="0 0 1600 500" preserveAspectRatio="none">
    <defs>
      <linearGradient id="engineTone" x1="0" y1="0" x2="1" y2="1">
        <stop offset="0" stop-color="#8494b2"/>
        <stop offset="0.5" stop-color="#4d6189"/>
        <stop offset="1" stop-color="#2c3f6c"/>
      </linearGradient>
      <linearGradient id="leftBlue" x1="0" y1="0" x2="1" y2="1">
        <stop offset="0" stop-color="#1a3bab"/>
        <stop offset="1" stop-color="#0b2684"/>
      </linearGradient>
      <linearGradient id="rightBlue" x1="0" y1="0" x2="1" y2="0">
        <stop offset="0" stop-color="#1536a6" stop-opacity="0.75"/>
        <stop offset="1" stop-color="#0f2c96" stop-opacity="0.95"/>
      </linearGradient>
      <linearGradient id="partTone" x1="0" y1="0" x2="0" y2="1">
        <stop offset="0" stop-color="#e4e6ea"/>
        <stop offset="0.55" stop-color="#b8bcc3"/>
        <stop offset="1" stop-color="#4a4e56"/>
      </linearGradient>
      <linearGradient id="whiteSweep" x1="0" y1="0" x2="1" y2="1">
        <stop offset="0" stop-color="#ffffff" stop-opacity="0"/>
        <stop offset="1" stop-color="#ffffff"/>
      </linearGradient>
    </defs>

    <rect x="0" y="0" width="1600" height="500" fill="url(#engineTone)" role="img" aria-label="Photo of an engine bay in muted blue tones"/>

    <polygon points="1440,0 1600,0 1600,500 900,500 965,250" fill="url(#rightBlue)"/>
    <polygon points="1600,300 1600,500 1180,500" fill="url(#whiteSweep)"/>

    <polygon points="510,0 600,0 360,180 300,124" fill="#d9dce2" opacity="0.6"/>
    <polygon points="0,300 300,124 470,240 470,500 0,500" fill="url(#leftBlue)"/>
    <polygon points="0,0 510,0 0,300" fill="#ffffff"/>

    <line x1="975" y1="460" x2="1600" y2="460" stroke="#ffffff" stroke-opacity="0.35" stroke-width="1"/>

    <ellipse cx="705" cy="310" rx="290" ry="145" transform="rotate(-28 705 310)"
             fill="url(#partTone)" role="img" aria-label="Photo of a remanufactured starter motor"/>
  </svg>

  <div class="brand">
    <span class="brand__dot"></span>
    <span class="brand__name">Ampvero</span>
  </div>

  <h1 class="headline">Alternators<br>&amp; Starters</h1>

  <div class="badge__ring"></div>
  <div class="badge">
    <span class="badge__value">100%</span>
    <span class="badge__label">Factory<br>Tested</span>
  </div>

  <div class="social">
    <span class="social__dot"></span>
    <span class="social__dot"></span>
    <span class="social__dot"></span>
    <span class="social__dot"></span>
  </div>

  <p class="intro">We offer premium quality<br>re-manufactured alternators and<br>starters. We are a<br>wholesaler/distributor that services<br>major auto-part stores with these<br>quality products.</p>

  <p class="contact">CALL TODAY <strong>1200-345-678</strong></p>
  <p class="site">www.ampvero.com</p>
</div>
</body>
</html>
```